E-mail Ad Design Project

I would like a lower banner ad designed for placement within an e-mail. The size has to be 450px x 230px (6in x 3.07in) and must be either a GIF or JPEG, not to exceed 30K.

We are a medical billing company that provides services to physical therapy practices in Florida, and this ad is intended for owners and office managers of physical therapy businesses. We provide therapy offices with practice management software, submit medical claims on behalf of their patients, follow-up with insurance companies on outstanding claims, and also perform necessary back-end collections with patient balances. We also are able to interface with popular therapy documentation products to streamline data entry.

The design colors should incorporate our logo and red/blue colors (see www.clinicianharbor.net).

Target Market(s)

Physical therapists and administrators of physical therapy offices

Industry/Entity Type

Physical Therapy

Requirements
Must have
• Grabbing/heading text:

Tired of Denials and Confusing Rejection Codes?
We Take the Pain Out of Medical Billing.

Offer:

Get Started Today with 2 Free Months of Billing
Nice to have
• We provide services mainly to Florida therapists, so it would be nice to have an image or text that highlights this fact. Also, the e-mail campaign this is a part of will be sent to Florida recipients.

```html
<!DOCTYPE html>
<html lang="en">
<head>
<meta charset="utf-8">
<title>Clinician Harbor – Medical Billing Banner</title>
<link href="https://fonts.googleapis.com/css2?family=Arimo:ital,wght@0,400;0,700;1,700&display=swap" rel="stylesheet">
<style>
  :root {
    --navy: #1c3a70;
    --blue-deep: #0f4fa3;
    --blue-mid: #2a7fd4;
    --blue-light: #7cc0f2;
    --sky-top: #ffffff;
    --sky-bottom: #d9ebf8;
    --red: #d4231f;
    --red-dark: #9e1412;
    --white: #ffffff;
    --photo-staff: #c9d9e6;
    --photo-office: #dfe9f1;
  }
  html, body {
    margin: 0;
    padding: 0;
    overflow: hidden;
  }
  body {
    width: 1200px;
    height: 613px;
    font-family: "Arimo", Arial, sans-serif;
  }
  .banner {
    position: relative;
    width: 1200px;
    height: 613px;
    overflow: hidden;
    background: linear-gradient(180deg, var(--sky-top) 0%, var(--sky-bottom) 100%);
  }
  .headline {
    position: absolute;
    top: 14px;
    left: 0;
    width: 1200px;
    margin: 0;
    text-align: center;
    font-weight: 700;
    font-size: 58px;
    line-height: 62px;
    color: var(--navy);
    letter-spacing: -0.5px;
  }
  .photo-office {
    position: absolute;
    left: 300px;
    top: 260px;
    width: 900px;
    height: 300px;
    background: linear-gradient(90deg, var(--photo-office) 0%, #eef4f9 100%);
  }
  .photo-staff {
    position: absolute;
    left: 0;
    top: 210px;
    width: 440px;
    height: 403px;
    background: linear-gradient(180deg, var(--photo-staff) 0%, #e7eef4 100%);
  }
  .shapes {
    position: absolute;
    left: 0;
    top: 0;
  }
  .tagline {
    position: absolute;
    left: 250px;
    top: 192px;
    width: 900px;
    margin: 0;
    text-align: center;
    color: var(--white);
    font-weight: 700;
    font-size: 38px;
    line-height: 44px;
    text-transform: uppercase;
  }
  .brand {
    position: absolute;
    left: 0;
    top: 520px;
    width: 427px;
    height: 72px;
    background: var(--white);
    display: flex;
    align-items: center;
    justify-content: center;
    color: var(--navy);
    font-weight: 700;
    font-size: 32px;
    letter-spacing: 1px;
    text-transform: uppercase;
  }
  .offer-badge {
    position: absolute;
    left: 928px;
    top: 212px;
    width: 270px;
    height: 270px;
  }
  .offer-text {
    position: absolute;
    left: 943px;
    top: 262px;
    width: 240px;
    margin: 0;
    text-align: center;
    color: var(--white);
    font-weight: 700;
    font-style: italic;
    transform: rotate(-12deg);
  }
  .offer-number {
    display: block;
    font-size: 76px;
    line-height: 80px;
  }
  .offer-label {
    display: block;
    font-size: 30px;
    line-height: 34px;
  }
  .cta {
    position: absolute;
    left: 758px;
    top: 487px;
    width: 429px;
    height: 112px;
    border-radius: 26px;
    border: 4px solid var(--blue-deep);
    box-sizing: border-box;
    background: linear-gradient(180deg, var(--blue-light) 0%, var(--blue-mid) 45%, var(--blue-deep) 100%);
    display: flex;
    align-items: center;
    justify-content: center;
    color: var(--white);
    font-weight: 700;
    font-size: 44px;
    text-decoration: none;
  }
</style>
</head>
<body>
  <main class="banner">
    <h1 class="headline">Tired of Denials &amp; Confusing<br>Rejection Codes?</h1>

    <div class="photo-office" role="img" aria-label="Photo of a medical billing office with staff at computers"></div>
    <div class="photo-staff" role="img" aria-label="Photo of a smiling clinician in a white coat with a stethoscope"></div>

    <svg class="shapes" width="1200" height="613" viewBox="0 0 1200 613" aria-hidden="true">
      <defs>
        <linearGradient id="ribbon-fill" x1="0" y1="0" x2="0" y2="1">
          <stop offset="0" stop-color="#5fb0ef"/>
          <stop offset="0.5" stop-color="#1d6fc4"/>
          <stop offset="1" stop-color="#0d4a9a"/>
        </linearGradient>
      </defs>
      <path d="M205 178 Q 700 148 1200 162 L1200 282 Q 700 318 205 290 Q 185 234 205 178 Z"
            fill="url(#ribbon-fill)" stroke="#ffffff" stroke-width="6"/>
    </svg>

    <p class="tagline">We take the pain out<br>of medical billing</p>

    <svg class="offer-badge" viewBox="-105 -105 210 210" aria-hidden="true">
      <polygon fill="var(--red)" stroke="var(--red-dark)" stroke-width="2"
        points="100,0 83.4,16.6 92.4,38.3 70.6,47.3 70.7,70.7 47.3,70.6 38.3,92.4 16.6,83.4 0,100 -16.6,83.4 -38.3,92.4 -47.3,70.6 -70.7,70.7 -70.6,47.3 -92.4,38.3 -83.4,16.6 -100,0 -83.4,-16.6 -92.4,-38.3 -70.6,-47.3 -70.7,-70.7 -47.3,-70.6 -38.3,-92.4 -16.6,-83.4 0,-100 16.6,-83.4 38.3,-92.4 47.3,-70.6 70.7,-70.7 70.6,-47.3 92.4,-38.3 83.4,-16.6"/>
    </svg>
    <p class="offer-text">
      <span class="offer-number">2</span>
      <span class="offer-label">free Months</span>
      <span class="offer-label">of Billing</span>
    </p>

    <div class="brand">Clinician Harbor</div>

    <a class="cta" href="#">Get Started NOW</a>
  </main>
</body>
</html>
```